Torvane Quill Hatch Back Full Wrap

I've decided to keep my current logo, but I want a full wrap on a 2010 Torvane Quill Hatchback, the current color is black.
dimensions are 169″ L x 67″ W x 60″ H
I want something like the picture below "abstract geometric" in red black and white.
It doesn't have to be that exactly but something "geometric" i'm going for a Rally Car look.
text to be:
"Brightbeam Builders logo" logo attached as "yard sign - v2"
Home renovations
239-555-0182
Licensed & Insured
(pretty much the whole yard sign other than soffit repair)
Then somewhere the "ask us about" info that's on the trailer photo
•Soffit & Siding (<-- changed from trailer graphics)
•Kitchen & Bath
•Cabinets & Backsplash
•Baseboard & Crown
•Flooring & Tile
•Drywall & Painting
My biggest concern is the logo and wording getting lost in the busyness of the background so i think we'll need a backdrop or "shadows" to separate the word from the design
The front windows can not be wrapped but the back can.
I would prefer mainly white on the top and hood going to black then red like the example photo attached.

Need extra days to review

```html
<!DOCTYPE html>
<html lang="en">
<head>
<meta charset="utf-8">
<title>Brightbeam Builders – Hatchback Wrap</title>
<link href="https://fonts.googleapis.com/css2?family=Roboto+Slab:wght@700&family=Roboto+Condensed:wght@700&display=swap" rel="stylesheet">
<style>
  :root {
    --wrap-red: #d71920;
    --wrap-red-dark: #a80f15;
    --wrap-black: #1b1b1d;
    --wrap-white: #ffffff;
    --tyre: #151515;
    --rim: #2e2e30;
    --page: #ffffff;
  }
  html, body {
    margin: 0;
    width: 1200px;
    height: 1200px;
    overflow: hidden;
    background: var(--page);
  }
  .canvas {
    position: relative;
    width: 1200px;
    height: 1200px;
  }
  .vehicle {
    position: absolute;
    left: 62px;
    width: 1075px;
    height: 412px;
  }
  .vehicle--red-hood { top: 120px; }
  .vehicle--white-hood { top: 660px; }
  .badge-text {
    font-family: "Roboto Slab", serif;
    font-weight: 700;
    font-size: 11px;
    fill: var(--wrap-white);
    letter-spacing: 0.3px;
  }
  .headline {
    font-family: "Roboto Slab", serif;
    font-weight: 700;
    font-size: 19px;
    fill: var(--wrap-red);
  }
  .phone {
    font-family: "Roboto Condensed", sans-serif;
    font-weight: 700;
    font-size: 30px;
    fill: var(--wrap-white);
    letter-spacing: 2px;
  }
  .services text {
    font-family: "Roboto Condensed", sans-serif;
    font-weight: 700;
    font-size: 8.5px;
    fill: var(--wrap-white);
  }
  .brand-name {
    font-family: "Roboto Slab", serif;
    font-weight: 700;
    fill: var(--wrap-white);
  }
</style>
</head>
<body>
<main class="canvas">

  <svg class="vehicle vehicle--red-hood" viewBox="0 0 860 330" role="img" aria-label="Side view of hatchback wrap with red hood">
    <defs>
      <clipPath id="body-a">
        <path d="M10 270 L5 200 Q8 150 45 140 L250 65 L380 8 L710 12 L760 58 L820 100 L845 150 L852 230 L835 272 L785 275 A72 72 0 0 0 645 275 L235 275 A72 72 0 0 0 90 275 Z"/>
      </clipPath>
      <linearGradient id="glass-a" x1="0" y1="0" x2="1" y2="1">
        <stop offset="0" stop-color="#f4f2ec"/>
        <stop offset="1" stop-color="#d8d3c6"/>
      </linearGradient>
    </defs>
    <ellipse class="ground-shadow" cx="430" cy="312" rx="410" ry="10" fill="#000" opacity="0.18"/>
    <g class="wrap-panels" clip-path="url(#body-a)">
      <rect class="panel-base" x="0" y="0" width="860" height="330" fill="var(--wrap-red)"/>
      <polygon class="panel-black-main" points="235,280 240,135 505,15 870,-5 870,175 600,225 250,280" fill="var(--wrap-black)"/>
      <polygon class="stripe-front-black" points="0,205 250,148 250,175 0,238" fill="var(--wrap-black)"/>
      <polygon class="stripe-front-white" points="0,242 200,195 200,203 0,252" fill="var(--wrap-white)"/>
      <polygon class="slash-white" points="505,15 575,-5 640,-5 545,38" fill="var(--wrap-white)"/>
      <polygon class="slash-red-roof" points="545,38 640,-5 660,-5 560,45" fill="var(--wrap-red)"/>
      <polygon class="stripe-lower-thin" points="240,262 870,170 870,175 240,267" fill="var(--wrap-red)"/>
      <polygon class="stripe-lower-red" points="240,270 870,178 870,213 240,285" fill="var(--wrap-red)"/>
      <polygon class="stripe-rocker-white" points="240,287 870,216 870,222 240,293" fill="var(--wrap-white)"/>
      <polygon class="rear-red-block" points="640,195 870,165 870,290 640,290" fill="var(--wrap-red-dark)" opacity="0.8"/>
      <polygon class="slash-front-top" points="200,110 255,85 255,100 210,120" fill="var(--wrap-red-dark)"/>
    </g>
    <path class="side-glass" d="M265 112 L345 40 Q400 22 495 22 L495 112 Z" fill="url(#glass-a)" stroke="#111" stroke-width="3"/>
    <path class="rear-light" d="M825 112 L848 150 L820 150 Z" fill="#b01218"/>
    <g class="badge" transform="translate(112 150) rotate(-8)">
      <rect x="0" y="0" width="130" height="17" rx="3" fill="var(--wrap-red)" stroke="var(--wrap-white)" stroke-width="1.5"/>
      <text class="badge-text" x="65" y="12.5" text-anchor="middle">LICENSED &amp; INSURED</text>
    </g>
    <text class="headline" x="265" y="194" transform="rotate(-5 265 194)">HOME RENOVATIONS</text>
    <text class="phone" x="266" y="226" transform="rotate(-5 266 226)">239-555-0182</text>
    <g class="services" transform="translate(310 238) rotate(-8.3)">
      <text x="0" y="0">• SOFFIT &amp; SIDING  • KITCHEN &amp; BATH  • CABINETS &amp; BACKSPLASH  • BASEBOARD &amp; CROWN</text>
      <text x="60" y="11">• FLOORING &amp; TILE  • DRYWALL &amp; PAINTING</text>
    </g>
    <g class="brand" transform="translate(500 140) rotate(-4)">
      <text class="brand-name" x="0" y="0" font-size="40">Brightbeam</text>
      <text class="brand-name" x="2" y="34" font-size="24">BUILDERS LLC</text>
    </g>
    <g class="wheel wheel--front">
      <circle cx="160" cy="268" r="60" fill="var(--tyre)"/>
      <circle cx="160" cy="268" r="42" fill="var(--rim)" stroke="#555" stroke-width="2"/>
      <circle cx="160" cy="268" r="8" fill="#111"/>
    </g>
    <g class="wheel wheel--rear">
      <circle cx="715" cy="268" r="60" fill="var(--tyre)"/>
      <circle cx="715" cy="268" r="42" fill="var(--rim)" stroke="#555" stroke-width="2"/>
      <circle cx="715" cy="268" r="8" fill="#111"/>
    </g>
  </svg>

  <svg class="vehicle vehicle--white-hood" viewBox="0 0 860 330" role="img" aria-label="Side view of hatchback wrap with white hood and roof">
    <defs>
      <clipPath id="body-b">
        <path d="M10 270 L5 200 Q8 150 45 140 L250 65 L380 8 L710 12 L760 58 L820 100 L845 150 L852 230 L835 272 L785 275 A72 72 0 0 0 645 275 L235 275 A72 72 0 0 0 90 275 Z"/>
      </clipPath>
      <linearGradient id="glass-b" x1="0" y1="0" x2="1" y2="1">
        <stop offset="0" stop-color="#f4f2ec"/>
        <stop offset="1" stop-color="#d8d3c6"/>
      </linearGradient>
    </defs>
    <ellipse class="ground-shadow" cx="430" cy="312" rx="410" ry="10" fill="#000" opacity="0.18"/>
    <g class="wrap-panels" clip-path="url(#body-b)">
      <rect class="panel-base" x="0" y="0" width="860" height="330" fill="var(--wrap-red)"/>
      <polygon class="panel-white-top" points="0,0 520,0 250,150 0,200" fill="var(--wrap-white)" stroke="#ccc" stroke-width="1"/>
      <polygon class="panel-black-main" points="235,280 240,150 505,15 870,-5 870,175 600,225 250,280" fill="var(--wrap-black)"/>
      <polygon class="stripe-front-red" points="0,200 250,150 250,160 0,212" fill="var(--wrap-red)"/>
      <polygon class="stripe-front-black" points="0,212 250,160 250,180 0,238" fill="var(--wrap-black)"/>
      <polygon class="stripe-front-white" points="0,242 200,195 200,203 0,252" fill="var(--wrap-white)"/>
      <polygon class="slash-red-roof" points="505,15 575,-5 660,-5 545,45" fill="var(--wrap-red)"/>
      <polygon class="stripe-lower-thin" points="240,262 870,170 870,175 240,267" fill="var(--wrap-red)"/>
      <polygon class="stripe-lower-red" points="240,270 870,178 870,213 240,285" fill="var(--wrap-red)"/>
      <polygon class="stripe-rocker-white" points="240,287 870,216 870,222 240,293" fill="var(--wrap-white)"/>
      <polygon class="rear-red-block" points="640,195 870,165 870,290 640,290" fill="var(--wrap-red-dark)" opacity="0.8"/>
    </g>
    <path class="side-glass" d="M265 112 L345 40 Q400 22 495 22 L495 112 Z" fill="url(#glass-b)" stroke="#111" stroke-width="3"/>
    <path class="rear-light" d="M825 112 L848 150 L820 150 Z" fill="#b01218"/>
    <g class="badge" transform="translate(112 150) rotate(-8)">
      <rect x="0" y="0" width="130" height="17" rx="3" fill="var(--wrap-red)" stroke="var(--wrap-white)" stroke-width="1.5"/>
      <text class="badge-text" x="65" y="12.5" text-anchor="middle">LICENSED &amp; INSURED</text>
    </g>
    <text class="headline" x="265" y="194" transform="rotate(-5 265 194)">HOME RENOVATIONS</text>
    <text class="phone" x="266" y="226" transform="rotate(-5 266 226)">239-555-0182</text>
    <g class="services" transform="translate(310 238) rotate(-8.3)">
      <text x="0" y="0">• SOFFIT &amp; SIDING  • KITCHEN &amp; BATH  • CABINETS &amp; BACKSPLASH  • BASEBOARD &amp; CROWN</text>
      <text x="60" y="11">• FLOORING &amp; TILE  • DRYWALL &amp; PAINTING</text>
    </g>
    <g class="brand" transform="translate(500 140) rotate(-4)">
      <text class="brand-name" x="0" y="0" font-size="40">Brightbeam</text>
      <text class="brand-name" x="2" y="34" font-size="24">BUILDERS LLC</text>
    </g>
    <g class="wheel wheel--front">
      <circle cx="160" cy="268" r="60" fill="var(--tyre)"/>
      <circle cx="160" cy="268" r="42" fill="var(--rim)" stroke="#555" stroke-width="2"/>
      <circle cx="160" cy="268" r="8" fill="#111"/>
    </g>
    <g class="wheel wheel--rear">
      <circle cx="715" cy="268" r="60" fill="var(--tyre)"/>
      <circle cx="715" cy="268" r="42" fill="var(--rim)" stroke="#555" stroke-width="2"/>
      <circle cx="715" cy="268" r="8" fill="#111"/>
    </g>
  </svg>

</main>
</body>
</html>
```